Business card design and logo for plumbing bussiness

We are wanting a logo for a plumbing business is Queensland Australia. KRV Plumbing and Drainage will be doing works on domestic and commercial sites.
Plumbing, drainage and gas works. We are wanting something that will stand out and be noticed. Colours could be black blue and white but open for suggestions.

Target Market(s)

Builders and home renovators

Industry/Entity Type

Plumbing

Contact Information for Business Card

Miles Dorgan - Director
0417 582 913
miles@krvplumbing.example.com.au
QBCC: 847 2106
ABN: 52 319 407 281

Font styles to use
Sans Serif

Colors
000000

Requirements
Must have
• Clear defined branding

```html
<!DOCTYPE html>
<html lang="en">
<head>
<meta charset="utf-8">
<title>KRV Plumbing and Drainage – Business Card</title>
<link rel="stylesheet" href="https://fonts.googleapis.com/css2?family=League+Gothic&family=Quicksand:wght@700&display=swap">
<style>
  :root {
    --ink-black: #000000;
    --deep-teal: #12302f;
    --mid-shadow: #061414;
    --paper-white: #ffffff;
  }
  html, body {
    margin: 0;
    padding: 0;
    width: 1200px;
    height: 720px;
    overflow: hidden;
    background: var(--ink-black);
  }
  .card {
    position: relative;
    width: 1200px;
    height: 720px;
    overflow: hidden;
    background: radial-gradient(ellipse 62% 70% at 50% 40%, var(--deep-teal) 0%, var(--mid-shadow) 55%, var(--ink-black) 100%);
    color: var(--paper-white);
  }
  .brand-mark {
    position: absolute;
    left: 0;
    right: 0;
    top: 223px;
    margin: 0;
    text-align: center;
    font-family: "League Gothic", "Oswald", sans-serif;
    font-weight: 400;
    font-size: 160px;
    line-height: 1;
    letter-spacing: 2px;
    color: var(--paper-white);
  }
  .brand-name {
    position: absolute;
    left: 0;
    right: 0;
    top: 468px;
    margin: 0;
    text-align: center;
    font-family: "League Gothic", "Oswald", sans-serif;
    font-weight: 400;
    font-size: 78px;
    line-height: 1;
    letter-spacing: 2px;
    text-transform: uppercase;
    color: var(--paper-white);
    transform: scaleX(0.68);
    transform-origin: 50% 50%;
  }
  .web-address {
    position: absolute;
    left: 0;
    right: 0;
    top: 600px;
    margin: 0;
    text-align: center;
    font-family: "Quicksand", "Nunito", sans-serif;
    font-weight: 700;
    font-size: 31px;
    line-height: 1;
    letter-spacing: 1px;
    color: var(--paper-white);
  }
</style>
</head>
<body>
  <main class="card">
    <div class="brand-mark">KRV</div>
    <h1 class="brand-name">KRV Plumbing and Drainage</h1>
    <p class="web-address">www.krvplumbing.example.com.au</p>
  </main>
</body>
</html>
```